Broschüre für Planungen und Verkauf von Häusern
Zielgruppe
Planungen und Verkauf von Häusern
Aufgabenstellung
Es sollte auf der Basis meines erstellten Logo und den Farben basieren. auf der vorderen Seite das Logo mit Firmennamen und
ein Spruch
Ein guter Plan heute, ist besser als ein perfekter Plan morgen
Innen aufklappbar mit zwei Laschen zum Einlegen von Angeboten usw. sowie einen Schlitz zum Einbringen von Visitenkarten
Rückseite Firmennamen Adressen Telefon usw.
Ein Beisdspiel lege ich bei, nur sollten die Farben angepasst werden

```html
<!DOCTYPE html>
<html lang="de">
<head>
<meta charset="utf-8">
<title>Baurix 17 GmbH – Präsentationsmappe</title>
<link href="https://fonts.googleapis.com/css2?family=Montserrat:wght@300;400;600;700&display=swap" rel="stylesheet">
<style>
  :root {
    --bg: #efefef;
    --paper: #f7f7f7;
    --paper-shade: #ebebeb;
    --brand-blue: #1f55ad;
    --brand-blue-deep: #0f3a8c;
    --brand-orange: #f3ad3b;
    --brand-orange-deep: #e8951d;
    --white: #ffffff;
    --ink: #1b1b1b;
    --ghost: #dfe4ec;
    --photo-light: #f1eeea;
    --photo-warm: #d9c8b6;
    --photo-mid: #c9b39d;
  }
  * { margin: 0; padding: 0; box-sizing: border-box; }
  html, body {
    width: 800px; height: 1200px; overflow: hidden;
    background: var(--bg);
    font-family: "Montserrat", sans-serif;
  }
  .canvas { position: relative; width: 800px; height: 1200px; }
  .outer-spread { position: absolute; left: 100px; top: 120px; width: 600px; height: 420px;
    box-shadow: 0 10px 24px rgba(0,0,0,.12); }
  .inner-spread { position: absolute; left: 50px; top: 730px; width: 440px; height: 310px;
    box-shadow: 0 8px 20px rgba(0,0,0,.1); }
  .front-single { position: absolute; left: 530px; top: 730px; width: 220px; height: 310px;
    box-shadow: 0 8px 20px rgba(0,0,0,.1); }
  svg { display: block; width: 100%; height: 100%; }
  .brand-name { font-family: "Montserrat", sans-serif; font-weight: 700; fill: var(--brand-blue); letter-spacing: .5px; }
  .brand-ghost { font-family: "Montserrat", sans-serif; font-weight: 700; fill: var(--ghost); letter-spacing: 2px; }
  .slogan { font-family: "Montserrat", sans-serif; font-weight: 300; fill: var(--white); letter-spacing: .4px; }
  .contact { font-family: "Montserrat", sans-serif; font-weight: 300; fill: var(--white); font-size: 8.5px; letter-spacing: .4px; }
  .register { font-family: "Montserrat", sans-serif; font-weight: 700; fill: var(--white); font-size: 8.5px; letter-spacing: .3px; }
  .card-label { font-family: "Montserrat", sans-serif; font-weight: 400; fill: var(--ink); font-size: 7.5px; }
</style>
</head>
<body>
<main class="canvas">

  <!-- Outer spread: back cover + front cover -->
  <section class="outer-spread">
    <svg viewBox="0 0 600 420" aria-label="Außenseite der Mappe">
      <defs>
        <linearGradient id="interiorWarm" x1="0" y1="0" x2="1" y2="1">
          <stop offset="0" stop-color="var(--photo-light)"/>
          <stop offset=".55" stop-color="var(--photo-warm)"/>
          <stop offset="1" stop-color="var(--photo-mid)"/>
        </linearGradient>
        <linearGradient id="interiorBright" x1="0" y1="0" x2="1" y2="1">
          <stop offset="0" stop-color="#f4f3f1"/>
          <stop offset=".6" stop-color="#e4ddd3"/>
          <stop offset="1" stop-color="#c7b7a3"/>
        </linearGradient>
      </defs>

      <!-- back cover -->
      <g class="back-cover">
        <rect class="photo-area" x="0" y="0" width="300" height="420" fill="url(#interiorWarm)" role="img" aria-label="Foto: helles Wohnzimmer mit Kamin und Sofa"/>
        <polygon class="band-orange" points="0,300 300,240 300,268 0,338" fill="var(--brand-orange)"/>
        <polygon class="band-white" points="0,338 300,268 300,274 0,348" fill="var(--white)"/>
        <polygon class="band-blue" points="0,348 300,274 300,420 0,420" fill="var(--brand-blue)"/>
        <text class="brand-name" x="40" y="96" font-size="17">BAURIX 17 GMBH</text>
        <text class="contact" x="276" y="312" text-anchor="end">LINDENALLEE 42</text>
        <text class="contact" x="276" y="326" text-anchor="end">10115 BERLIN</text>
        <text class="contact" x="276" y="340" text-anchor="end">0176 - 421 57 30</text>
        <text class="contact" x="276" y="354" text-anchor="end">R.HOLLWEG@MAILPOST.DE</text>
        <text class="register" x="40" y="388">HRB 318427 B</text>
        <text class="register" x="40" y="401">GF RAINER HOLLWEG</text>
      </g>

      <!-- front cover -->
      <g class="front-cover" transform="translate(300,0)">
        <rect class="photo-area" x="0" y="0" width="300" height="420" fill="url(#interiorBright)" role="img" aria-label="Foto: lichtdurchflutetes Wohnzimmer mit Bild, Baum und Sessel"/>
        <polygon class="band-orange" points="0,240 300,232 300,300 0,268" fill="var(--brand-orange-deep)"/>
        <polygon class="band-white" points="0,268 300,300 300,306 0,274" fill="var(--white)"/>
        <polygon class="band-blue" points="0,274 300,306 300,420 0,420" fill="var(--brand-blue-deep)"/>
        <text class="brand-name" x="270" y="66" font-size="17" text-anchor="end">BAURIX 17 GMBH</text>
        <text class="slogan" x="28" y="352" font-size="12.5">EIN GUTER PLAN HEUTE,</text>
        <text class="slogan" x="28" y="370" font-size="12.5">IST BESSER ALS EIN</text>
        <text class="slogan" x="28" y="388" font-size="12.5">PERFEKTER PLAN MORGEN</text>
      </g>
      <line class="fold" x1="300" y1="0" x2="300" y2="420" stroke="rgba(0,0,0,.08)" stroke-width="1"/>
    </svg>
  </section>

  <!-- Inner spread with business card pocket -->
  <section class="inner-spread">
    <svg viewBox="0 0 440 310" aria-label="Innenseite der Mappe mit Visitenkartenlasche">
      <defs>
        <linearGradient id="innerPaper" x1="0" y1="0" x2="1" y2="0">
          <stop offset="0" stop-color="var(--paper)"/>
          <stop offset=".48" stop-color="var(--white)"/>
          <stop offset=".5" stop-color="var(--paper-shade)"/>
          <stop offset="1" stop-color="var(--paper)"/>
        </linearGradient>
      </defs>
      <rect class="inner-paper" x="0" y="0" width="440" height="310" fill="url(#innerPaper)"/>
      <text class="brand-ghost" x="220" y="140" font-size="30" text-anchor="middle">BAURIX 17 GMBH</text>
      <path class="pocket" d="M220,310 L220,250 Q222,226 248,226 L440,226 L440,310 Z" fill="var(--brand-blue)"/>
      <polygon class="pocket-orange" points="220,310 440,270 440,310" fill="var(--brand-orange)"/>
      <line class="pocket-line" x1="220" y1="305" x2="440" y2="265" stroke="var(--white)" stroke-width="2"/>
      <rect class="card-slot" x="258" y="238" width="88" height="56" fill="var(--white)"/>
      <text class="card-label" x="302" y="263" text-anchor="middle">IHR</text>
      <text class="card-label" x="302" y="273" text-anchor="middle">VISITENKARTE</text>
    </svg>
  </section>

  <!-- Front cover alone -->
  <section class="front-single">
    <svg viewBox="0 0 220 310" aria-label="Titelseite">
      <rect class="photo-area" x="0" y="0" width="220" height="310" fill="url(#interiorBright)" role="img" aria-label="Foto: lichtdurchflutetes Wohnzimmer mit Bild, Baum und Sessel"/>
      <polygon class="band-orange" points="0,195 220,195 220,230 0,198" fill="var(--brand-orange)"/>
      <polygon class="band-white" points="0,198 220,230 220,234 0,202" fill="var(--white)"/>
      <polygon class="band-blue" points="0,202 220,234 220,310 0,310" fill="var(--brand-blue)"/>
      <text class="brand-name" x="206" y="44" font-size="12" text-anchor="end">BAURIX 17 GMBH</text>
      <text class="slogan" x="16" y="257" font-size="9.5">EIN GUTER PLAN HEUTE,</text>
      <text class="slogan" x="16" y="271" font-size="9.5">IST BESSER ALS EIN</text>
      <text class="slogan" x="16" y="285" font-size="9.5">PERFEKTER PLAN MORGEN</text>
    </svg>
  </section>

</main>
</body>
</html>
```